Quorlan Visit cards serious but not sad

Hello, I'd like to design my visit cards with the logo Quorlan (attached) the following information: Name: Mathis Deloraux Title: Mobile Director: 33 (0) 6 28 40 13 85 Phone: 33 (0) 4 71 86 52 09 e-mail: mathis.deloraux@quorlan-advisory.example address: 17 Rue Anatole Berrin 92400 Courbevoie This visit will be used on the banking institutions and Quorlan is a consulting firm. I do not want to have dark background.

Target Market(s)

banks

Contact Information for Business Card

Name : Mathis Deloraux
Title : Director
mobile : +33(0)6 28 40 13 85
Phone : +33(0)4 71 86 52 09
e-mail: mathis.deloraux@quorlan-advisory.example
adresse : 17 Rue anatole Berrin 92400 Courbevoie

Requirements
Nice to have
• serious but not sad

```html
<!DOCTYPE html>
<html lang="en">
<head>
<meta charset="utf-8">
<title>Quorlan – Business Card</title>
<link rel="stylesheet" href="https://fonts.googleapis.com/css2?family=Exo+2:wght@500;600&family=Roboto:wght@400&display=swap">
<style>
  :root {
    --page-bg: #d9d6d1;
    --card-bg: #eef0f2;
    --card-edge: #c9cdd2;
    --brand-blue: #2d5f9b;
    --text-dark: #2b2b2b;
    --text-muted: #4a4a4a;
  }
  html, body {
    margin: 0;
    padding: 0;
    width: 1200px;
    height: 1054px;
    overflow: hidden;
    background: var(--page-bg);
  }
  .business-card {
    position: absolute;
    left: 100px;
    top: 225px;
    width: 1000px;
    height: 603px;
    background: var(--card-bg);
    border: 1px solid var(--card-edge);
    overflow: hidden;
    font-family: "Roboto", Arial, sans-serif;
  }
  .brand {
    position: absolute;
    left: 43px;
    top: 51px;
    display: flex;
    align-items: center;
    gap: 12px;
  }
  .brand-dot {
    width: 90px;
    height: 90px;
    border-radius: 50%;
    background: var(--brand-blue);
  }
  .brand-name {
    font-family: "Exo 2", Arial, sans-serif;
    font-weight: 500;
    font-size: 72px;
    line-height: 1;
    color: var(--brand-blue);
    letter-spacing: 1px;
  }
  .feature-circle {
    position: absolute;
    left: 543px;
    top: 77px;
    width: 482px;
    height: 482px;
    border-radius: 50%;
    background: var(--brand-blue);
  }
  .person-name {
    position: absolute;
    left: 48px;
    top: 282px;
    margin: 0;
    font-family: "Exo 2", Arial, sans-serif;
    font-weight: 600;
    font-size: 43px;
    color: var(--brand-blue);
  }
  .person-title {
    position: absolute;
    left: 49px;
    top: 346px;
    margin: 0;
    font-size: 22px;
    color: var(--text-muted);
  }
  .contact-list {
    position: absolute;
    left: 50px;
    top: 418px;
    margin: 0;
    padding: 0;
    list-style: none;
  }
  .contact-item {
    display: flex;
    align-items: center;
    height: 34px;
    font-size: 24px;
    color: var(--text-dark);
  }
  .contact-icon {
    width: 22px;
    height: 22px;
    margin-right: 16px;
    fill: var(--brand-blue);
  }
  .address {
    position: absolute;
    left: 48px;
    top: 528px;
    margin: 0;
    font-size: 24px;
    color: var(--text-dark);
  }
</style>
</head>
<body>
  <article class="business-card">
    <div class="feature-circle"></div>

    <header class="brand">
      <div class="brand-dot"></div>
      <span class="brand-name">quorlan</span>
    </header>

    <h1 class="person-name">Mathis Deloraux</h1>
    <p class="person-title">Director</p>

    <ul class="contact-list">
      <li class="contact-item">
        <svg class="contact-icon" viewBox="0 0 24 24" aria-hidden="true">
          <path d="M7 1h10a2 2 0 0 1 2 2v18a2 2 0 0 1-2 2H7a2 2 0 0 1-2-2V3a2 2 0 0 1 2-2zm0 3v14h10V4H7zm5 15.5a1.2 1.2 0 1 0 0 2.4 1.2 1.2 0 0 0 0-2.4z"/>
        </svg>
        +33(0)6 28 40 13 85
      </li>
      <li class="contact-item">
        <svg class="contact-icon" viewBox="0 0 24 24" aria-hidden="true">
          <path d="M2 8c0-2 4-4 10-4s10 2 10 4v2h-5V8c-1-.6-3-1-5-1s-4 .4-5 1v2H2V8zm5 3h10l3 8H4l3-8zm5 1.5a2.5 2.5 0 1 0 0 5 2.5 2.5 0 0 0 0-5z"/>
        </svg>
        +33(0)4 71 86 52 09
      </li>
      <li class="contact-item">
        <svg class="contact-icon" viewBox="0 0 24 24" aria-hidden="true">
          <path d="M2 5h20v14H2V5zm2 2v.4l8 5.6 8-5.6V7H4zm0 2.8V17h16V9.8l-8 5.6-8-5.6z"/>
        </svg>
        mathis.deloraux@quorlan-advisory.example
      </li>
    </ul>

    <p class="address">17 Rue anatole Berrin 92400 Courbevoie</p>
  </article>
</body>
</html>
```